Podcast Graphics For Internet Business Building Podcast

We need new podcast graphics.
1400x1400
300dpi

Needs to include text "Quiet Harbor Ledger Hour" as the podcast title and "Practical Online Venture Insights" as a subtitle.

We like blue and grey as our main colors, but are open to other schemes.

Please see attached image for an example of podcast graphics we like. While we prefer a more plain look, it would be nice to have a subtle hint related to a "machine" in the background. Something like a pencil sketch of cogs like on the Quiet Harbor Ledger 10 book cover (attached image).

Target Market(s)

online entrepreneurs or those who want to start an online business

Font styles to use
Sans Serif

Colors
0455a3
3277b5

Requirements
Must have
• Text noted in project description
Should not have
• No money symbols or flashy "make money" type things.

```html
<!DOCTYPE html>
<html lang="en">
<head>
<meta charset="utf-8">
<title>Quiet Harbor Ledger Hour – Podcast Cover</title>
<link rel="stylesheet" href="https://fonts.googleapis.com/css2?family=Oswald:wght@600&family=Tenor+Sans&display=swap">
<style>
  :root {
    --blue-deep: #1a3272;
    --blue-mid: #0455a3;
    --blue-glow: #0a6fb6;
    --blue-soft: #3277b5;
    --title-ice: #cde6f7;
    --frame-line: #8fcaf2;
    --subtitle-white: #ffffff;
  }
  html, body {
    margin: 0;
    padding: 0;
    width: 1200px;
    height: 1200px;
    overflow: hidden;
    background: var(--blue-deep);
  }
  .cover {
    position: relative;
    width: 1200px;
    height: 1200px;
    overflow: hidden;
    background: radial-gradient(circle at 52% 48%, var(--blue-glow) 0%, var(--blue-mid) 38%, #0b4288 68%, var(--blue-deep) 100%);
  }
  .cover-art {
    position: absolute;
    inset: 0;
    width: 1200px;
    height: 1200px;
  }
  .cog-field {
    position: absolute;
    left: 820px;
    top: 0;
    width: 380px;
    height: 800px;
    background: radial-gradient(ellipse at 60% 40%, rgba(80, 150, 210, 0.32) 0%, rgba(60, 130, 200, 0.15) 45%, rgba(50, 119, 181, 0) 72%);
  }
  .light-sweep {
    position: absolute;
    left: 0;
    top: 150px;
    width: 1200px;
    height: 360px;
    background: radial-gradient(ellipse at 70% 50%, rgba(60, 170, 200, 0.14) 0%, rgba(60, 150, 200, 0.06) 45%, rgba(50, 119, 181, 0) 70%);
  }
  .title-line {
    font-family: "Oswald", "Arial Narrow", sans-serif;
    font-weight: 600;
    font-size: 140px;
    fill: var(--title-ice);
  }
  .subtitle {
    font-family: "Tenor Sans", sans-serif;
    font-size: 41px;
    fill: var(--subtitle-white);
    letter-spacing: 1px;
  }
</style>
</head>
<body>
  <main class="cover">
    <div class="light-sweep" role="img" aria-label="Faint flowing light lines across the background"></div>
    <div class="cog-field" role="img" aria-label="Faint sketch of interlocking cogs suggesting a machine"></div>

    <svg class="cover-art" viewBox="0 0 1200 1200" xmlns="http://www.w3.org/2000/svg">
      <rect class="inner-frame" x="86" y="80" width="1024" height="1034" fill="none" stroke="var(--frame-line)" stroke-width="2"/>

      <g class="podcast-title" aria-label="Quiet Harbor Ledger Hour" text-anchor="middle">
        <text class="title-line" x="598" y="400">QUIET</text>
        <text class="title-line" x="598" y="545">HARBOR</text>
        <text class="title-line" x="598" y="690">LEDGER</text>
        <text class="title-line" x="598" y="835">HOUR</text>
      </g>

      <text class="subtitle" x="598" y="1085" text-anchor="middle">PRACTICAL ONLINE VENTURE INSIGHTS</text>
    </svg>
  </main>
</body>
</html>
```